The Fernway Workshop Business Card

Create a single sided business card using the provided logo.
Use logo 1 in the zip file.

Information on the card:

Marisa Toller B.Ed(Ind Arts)
Partner - Instructor
Phone: (0412) 538 914
Email: marisa@fernwayworkshop.com.au
Website: www.fernwayworkshop.com.au
Facebook: www.facebook.com/FernwayWorkshopAU
Instagram: www.instagram.com/fernway_workshop_au

text colour to be rgb(117,165,22)
background colour (card stock) white.

```html
<!DOCTYPE html>
<html lang="en">
<head>
<meta charset="utf-8">
<title>The Fernway Workshop – Business Card</title>
<link rel="stylesheet" href="https://fonts.googleapis.com/css2?family=Arimo:wght@400;700&display=swap">
<style>
  :root {
    --brand-green: rgb(117,165,22);
    --card-green: rgb(138,190,48);
    --card-white: #ffffff;
    --ink-grey: #4a4a4a;
    --rule-grey: #555555;
    --backdrop: #e6e6e4;
  }
  * { box-sizing: border-box; margin: 0; padding: 0; }
  html, body { width: 1200px; height: 801px; overflow: hidden; }
  body {
    background: var(--backdrop);
    font-family: 'Arimo', Arial, sans-serif;
    position: relative;
  }
  .card {
    position: absolute;
    top: 240px;
    width: 525px;
    height: 300px;
    box-shadow: 0 6px 18px rgba(0,0,0,0.18);
  }
  .card--front { left: 50px; background: var(--card-white); }
  .card--back  { left: 625px; background: var(--card-green); }

  .brand {
    position: absolute;
    display: flex;
    align-items: center;
    gap: 12px;
    font-weight: 700;
    letter-spacing: 0.5px;
  }
  .brand__mark {
    width: 46px; height: 46px;
    border-radius: 50%;
    border: 4px solid currentColor;
    flex: none;
  }
  .brand__name { font-size: 26px; line-height: 1.05; }
  .card--front .brand { color: var(--brand-green); right: 36px; top: 42px; }
  .card--back .brand {
    color: var(--card-white);
    left: 50%; top: 50%;
    transform: translate(-50%, -50%);
  }
  .card--back .brand__mark { width: 60px; height: 60px; }
  .card--back .brand__name { font-size: 30px; }

  .person { position: absolute; left: 36px; top: 86px; }
  .person__name { color: var(--brand-green); font-weight: 700; font-size: 22px; }
  .person__role { color: var(--ink-grey); font-size: 15px; margin-top: 4px; }

  .divider {
    position: absolute;
    left: 36px; right: 36px; top: 152px;
    border-top: 1.5px solid var(--rule-grey);
  }

  .contacts { position: absolute; top: 170px; list-style: none; }
  .contacts--direct { left: 36px; }
  .contacts--social { right: 36px; }
  .contacts li {
    display: flex; align-items: center; gap: 8px;
    color: var(--ink-grey); font-size: 14px; line-height: 24px;
  }
  .contacts svg { width: 14px; height: 14px; flex: none; fill: var(--brand-green); }
  .contacts .dot {
    width: 12px; height: 12px; border-radius: 2px;
    background: var(--brand-green); flex: none;
  }
</style>
</head>
<body>
  <section class="card card--front" aria-label="Business card front">
    <div class="brand">
      <span class="brand__mark"></span>
      <span class="brand__name">The Fernway<br>Workshop</span>
    </div>

    <div class="person">
      <p class="person__name">Marisa Toller B.Ed</p>
      <p class="person__role">Partner / Instructor</p>
    </div>

    <div class="divider"></div>

    <ul class="contacts contacts--direct">
      <li>
        <svg viewBox="0 0 24 24" aria-hidden="true"><path d="M6.6 10.8a15.1 15.1 0 0 0 6.6 6.6l2.2-2.2a1 1 0 0 1 1-.25 11.4 11.4 0 0 0 3.6.57 1 1 0 0 1 1 1V20a1 1 0 0 1-1 1A17 17 0 0 1 3 4a1 1 0 0 1 1-1h3.5a1 1 0 0 1 1 1c0 1.25.2 2.45.57 3.57a1 1 0 0 1-.25 1z"/></svg>
        (0412) 538 914
      </li>
      <li>
        <svg viewBox="0 0 24 24" aria-hidden="true"><path d="M2 5h20v14H2z M2 5l10 8 10-8" fill="none" stroke="rgb(117,165,22)" stroke-width="2.4"/></svg>
        marisa@fernwayworkshop.com.au
      </li>
      <li>
        <svg viewBox="0 0 24 24" aria-hidden="true"><circle cx="12" cy="12" r="9" fill="none" stroke="rgb(117,165,22)" stroke-width="2.4"/><path d="M3 12h18M12 3c3 3 3 15 0 18M12 3c-3 3-3 15 0 18" fill="none" stroke="rgb(117,165,22)" stroke-width="1.8"/></svg>
        www.fernwayworkshop.com.au
      </li>
    </ul>

    <ul class="contacts contacts--social">
      <li><span class="dot"></span>FernwayWorkshopAU</li>
      <li><span class="dot"></span>fernway_workshop_au</li>
    </ul>
  </section>

  <section class="card card--back" aria-label="Business card back">
    <div class="brand">
      <span class="brand__mark"></span>
      <span class="brand__name">The Fernway<br>Workshop</span>
    </div>
  </section>
</body>
</html>
```